Webshop for baby shoes need new design

We are an innovative company selling a one of a kind product on a market with tough competition. We are looking to step up our business and need a new design for our shop.

We are looking for recognition as well as originality. The customer must immediately be able to identify navigation, shopping cart, buy buttons etc. We want warm welcoming colors, but not too strong as to not draw attention away from the products. Retro might be interesting, if "done right".

Suggested color palette: http://huepalettemaker.example/#7k29WbQx3p8r5

We have a logo (attached), but if you have a better idea we might go for that instead. Also, a couple of product images are attached for you to use in the design.

What we do NOT want is a shop that looks like a free template (vendaForge etc). Also, while we are selling baby shoes, we don't want to use the very worn our baby pink/blue scheme, so stay clear of this, thanks.
Updates

We suggest that you use this palette, or similar: http://huepalettemaker.example/#7k29WbQx3p8r5

Project Deadline Extended
Reason: We feel that we are getting closer to finding a design that we like, but there is still a bit to go. Also we want to give the chance to any late starters to show their idea. The competition is still open.

Target Market(s)

babies and their parents

Industry/Entity Type

Shopping

Requirements
Must have
• The usual webshop elements
- shopping cart
- product listing
- product page
- buy buttons
Nice to have
• - large footer area for links, info and function (see trindel.example for an example)
- some kind of product navigation/filter (left, top or right)
- place for promotion banners

```html
<!DOCTYPE html>
<html lang="en">
<head>
<meta charset="utf-8">
<title>Tossaro – Baby Shoes</title>
<link rel="stylesheet" href="https://fonts.googleapis.com/css2?family=Questrial&family=Jost:wght@500;600;700&display=swap">
<style>
:root{
  --page:#f3f2f0;
  --panel:#ffffff;
  --line:#dcdad6;
  --brown-light:#dca964;
  --brown-mid:#c08642;
  --brown-dark:#9c6128;
  --ink:#3b2a1a;
  --ink-soft:#5a5550;
  --title-brown:#6b3f12;
  --accent:#c4521d;
  --accent-soft:#c98046;
  --green:#9cc95b;
  --red:#e0585b;
  --blue:#5a8dc0;
  --footer:#6d4016;
  --footer-box:#58320f;
  --footer-bar:#4a2a0c;
  --footer-text:#f4e6d4;
}
*{box-sizing:border-box;margin:0;padding:0}
html,body{width:1089px;height:1200px;overflow:hidden}
body{background:var(--page);font-family:"Questrial",sans-serif;color:var(--ink);position:relative}
ul{list-style:none}

/* header */
.site-header{position:absolute;left:0;top:0;width:1089px;height:78px;border-bottom:1px solid #e2e0dc;background:#f6f5f3}
.brand{position:absolute;left:157px;top:14px;display:flex;align-items:center;gap:10px}
.brand-mark{width:44px;height:44px;border-radius:8px;background:var(--brown-mid)}
.brand-name{font-family:"Jost",sans-serif;font-weight:700;font-size:38px;color:var(--brown-dark);letter-spacing:1px}
.account-bar{position:absolute;left:640px;top:4px;width:291px;height:26px;background:#fff;border:1px solid var(--line);border-top:none;border-radius:0 0 6px 6px;box-shadow:0 2px 3px rgba(0,0,0,.12);display:flex;align-items:center;font-size:10px;color:#333}
.account-bar span{padding:0 11px;border-right:1px solid #c9c6c1;line-height:12px;white-space:nowrap}
.account-bar span:last-child{border:none}
.social{position:absolute;left:798px;top:45px;display:flex;gap:6px;font-size:10.5px;color:#333;align-items:center}
.social i{display:inline-block;width:14px;height:14px;background:#777;border-radius:2px;margin-right:4px;vertical-align:-3px}

/* nav */
.main-nav{position:absolute;left:157px;top:78px;width:775px;height:38px;border-radius:0 0 4px 4px;background:linear-gradient(var(--brown-light),var(--brown-dark));box-shadow:0 2px 3px rgba(0,0,0,.25);display:flex}
.main-nav a{font-family:"Jost",sans-serif;font-weight:600;font-size:10.5px;color:#fff;text-decoration:none;padding:0 20px;line-height:38px;border-right:1px solid rgba(90,50,15,.45);text-shadow:0 1px 1px rgba(0,0,0,.4)}

/* sidebar */
.category-list{position:absolute;left:157px;top:129px;width:146px;height:307px;background:var(--panel);border:1px solid var(--line)}
.category-list h3{font-family:"Jost",sans-serif;font-weight:600;font-size:11.5px;color:var(--title-brown);margin:9px 0 0 10px}
.category-list ul{margin-top:2px}
.category-list li{font-size:11.5px;color:#222;margin-left:24px;line-height:27.4px;position:relative}
.category-list li::before{content:"";position:absolute;left:-12px;top:12px;width:5px;height:5px;border-radius:50%;background:#222}

/* hero */
.hero{position:absolute;left:312px;top:129px;width:620px;height:307px;background:var(--panel);border:1px solid var(--line)}
.hero-title{position:absolute;left:30px;top:27px;font-family:"Jost",sans-serif;font-weight:600;font-size:37px;line-height:45px;letter-spacing:1px}
.hero-title .l1{color:var(--green)}.hero-title .l2{color:var(--red)}.hero-title .l3{color:var(--blue)}
.hero-sub{position:absolute;left:31px;top:191px;font-family:"Jost",sans-serif;font-weight:500;font-size:14px;color:var(--accent-soft)}
.btn{position:absolute;left:31px;top:218px;width:81px;height:38px;border-radius:4px;background:linear-gradient(var(--brown-light),var(--brown-dark));box-shadow:0 2px 3px rgba(0,0,0,.3);color:#fff;font-family:"Jost",sans-serif;font-weight:600;font-size:13px;text-align:center;line-height:38px;text-shadow:0 1px 1px rgba(0,0,0,.4)}
.hero-photo{position:absolute;left:233px;top:8px;width:372px;height:291px;background:radial-gradient(ellipse at 55% 55%,#e8e8ea 0%,#c9cfdc 45%,#fbfbfb 80%);border-radius:4px}
.slider-dots{position:absolute;right:14px;top:14px;display:flex;gap:5px}
.slider-dots span{width:17px;height:17px;border-radius:50%;background:#222}
.slider-dots span.on{background:#fff;border:3px solid #333}

/* news bar */
.news-bar{position:absolute;left:157px;top:445px;width:775px;height:38px;background:linear-gradient(var(--brown-light),var(--brown-mid));box-shadow:0 2px 3px rgba(0,0,0,.2);font-size:11.5px;line-height:38px;padding:0 13px;color:#2a1a0a;white-space:nowrap}
.news-bar b{font-family:"Jost",sans-serif;font-weight:600}
.news-bar .more{position:absolute;right:26px;top:0;font-family:"Jost",sans-serif;font-weight:600}

/* products */
.products{position:absolute;left:157px;top:493px;width:775px;height:354px;border-top:3px solid #cfccc7}
.products h2{height:35px;background:#fbfbfa;border:1px solid var(--line);border-top:none;text-align:center;font-family:"Jost",sans-serif;font-weight:600;font-size:10.5px;line-height:35px;color:#555;letter-spacing:.5px}
.product-grid{display:grid;grid-template-columns:repeat(4,1fr);gap:2px 0}
.product-card{height:157px;background:var(--panel);border:1px solid var(--line);position:relative;text-align:center}
.product-photo{position:absolute;left:28px;top:8px;width:136px;height:94px;border-radius:6px}
.p-blue{background:radial-gradient(ellipse,#2c4a86 30%,#7fb0de 60%,#fff 75%)}
.p-navy{background:radial-gradient(ellipse,#233d73 30%,#e07a3a 55%,#fff 75%)}
.p-white{background:radial-gradient(ellipse,#efece3 35%,#dcd8cf 55%,#fff 75%)}
.p-teal{background:radial-gradient(ellipse,#1f5c7e 35%,#3b7fa0 55%,#fff 75%)}
.product-name{position:absolute;left:0;right:0;top:110px;font-family:"Jost",sans-serif;font-weight:600;font-size:10.5px;line-height:10px;color:var(--title-brown)}
.product-price{position:absolute;left:0;right:0;top:136px;font-family:"Jost",sans-serif;font-weight:600;font-size:10.5px;color:#222}

/* promos */
.promos{position:absolute;left:157px;top:866px;width:775px;height:137px;background:var(--panel);border:1px solid var(--line);border-top:2px solid #cfccc7;box-shadow:0 2px 3px rgba(0,0,0,.12);display:flex}
.promo{flex:1;position:relative}
.promo+.promo{border-left:1px solid var(--line)}
.promo h4{height:35px;line-height:35px;padding-left:17px;border-bottom:1px solid var(--line);font-family:"Jost",sans-serif;font-weight:600;font-size:10.5px;color:#666;letter-spacing:.5px}
.promo p{padding:17px 14px 0 17px;font-size:11.5px;line-height:13.6px;color:#555}
.promo .more{position:absolute;right:15px;bottom:16px;font-family:"Jost",sans-serif;font-weight:600;font-size:11px;color:var(--accent)}
.deal{text-align:center;font-family:"Jost",sans-serif;font-weight:600;font-size:37px;line-height:36px;color:var(--accent);padding-top:9px;letter-spacing:1px;white-space:nowrap}

/* footer */
.site-footer{position:absolute;left:0;top:1037px;width:1089px;height:133px;background:var(--footer);color:var(--footer-text);font-size:11.5px}
.f-col{position:absolute;top:10px}
.f-col h5{font-weight:400;font-size:11.5px;padding-bottom:4px;border-bottom:1px solid #a57a4d;margin-bottom:3px}
.f-col li{line-height:24.2px;padding-left:4px;white-space:nowrap}
.f-col li::before{content:"• "}
.f-menu{left:157px;width:54px}
.f-menu ul{width:80px}
.f-box{position:absolute;left:567px;top:16px;width:342px;height:105px;background:var(--footer-box);border-radius:4px;padding:10px 11px;line-height:13.6px;font-size:11.2px}
.f-box .more{position:absolute;right:16px;bottom:13px;font-family:"Jost",sans-serif;font-weight:600;color:#e0662a}
.legal{position:absolute;left:0;top:1170px;width:1089px;height:30px;background:var(--footer-bar);color:#fff;text-align:center;font-size:11.5px;line-height:30px}
.legal b{font-weight:400;color:#231306}
</style>
</head>
<body>

<header class="site-header">
  <div class="brand"><span class="brand-mark"></span><span class="brand-name">Tossaro</span></div>
  <div class="account-bar"><span>REGISTER</span><span>LOGIN</span><span>CART 00</span><span>AMOUNT (0.00 $)</span></div>
  <div class="social"><span><i></i>Friendbook</span><span><i></i>Chirpline</span></div>
</header>

<nav class="main-nav">
  <a>HOME</a><a>PRODUCTS</a><a>CATEGORIES</a><a>CART</a><a>ABOUT</a><a>CONTACT</a>
</nav>

<aside class="category-list">
  <h3>CATEGORIES</h3>
  <ul>
    <li>Category-01</li><li>Category-02</li><li>Category-03</li><li>Category-04</li><li>Category-05</li>
    <li>Category-06</li><li>Category-07</li><li>Category-08</li><li>Category-09</li><li>Category-10</li>
  </ul>
</aside>

<section class="hero">
  <h1 class="hero-title"><span class="l1">HEADING</span><br><span class="l2">GOES</span><br><span class="l3">HERE . . .</span></h1>
  <div class="hero-sub">Browse More Products</div>
  <div class="btn">Products</div>
  <div class="hero-photo" role="img" aria-label="Pair of navy and white baby shoes with labelled feature callouts"></div>
  <div class="slider-dots"><span></span><span></span><span class="on"></span></div>
</section>

<div class="news-bar"><b>Latest Tweet or News :</b> Lorem ipsum dolor sit amet, consectetuer adipiscing elit, sed diam nonummy nibh<span class="more">READ MORE</span></div>

<section class="products">
  <h2>OUR PRODUCTS</h2>
  <div class="product-grid">
    <div class="product-card"><div class="product-photo p-blue" role="img" aria-label="Blue lace-up baby shoe"></div><div class="product-name">Product Code or<br>Name</div><div class="product-price">5,50 $</div></div>
    <div class="product-card"><div class="product-photo p-navy" role="img" aria-label="Navy and orange baby shoe"></div><div class="product-name">Product Code or<br>Name</div><div class="product-price">5,50 $</div></div>
    <div class="product-card"><div class="product-photo p-white" role="img" aria-label="White leather baby shoe"></div><div class="product-name">Product Code or<br>Name</div><div class="product-price">5,50 $</div></div>
    <div class="product-card"><div class="product-photo p-teal" role="img" aria-label="Teal strap baby shoe"></div><div class="product-name">Product Code or<br>Name</div><div class="product-price">5,50 $</div></div>
    <div class="product-card"><div class="product-photo p-blue" role="img" aria-label="Blue lace-up baby shoe"></div><div class="product-name">Product Code or<br>Name</div><div class="product-price">5,50 $</div></div>
    <div class="product-card"><div class="product-photo p-navy" role="img" aria-label="Navy and orange baby shoe"></div><div class="product-name">Product Code or<br>Name</div><div class="product-price">5,50 $</div></div>
    <div class="product-card"><div class="product-photo p-white" role="img" aria-label="White leather baby shoe"></div><div class="product-name">Product Code or<br>Name</div><div class="product-price">5,50 $</div></div>
    <div class="product-card"><div class="product-photo p-teal" role="img" aria-label="Teal strap baby shoe"></div><div class="product-name">Product Code or<br>Name</div><div class="product-price">5,50 $</div></div>
  </div>
</section>

<section class="promos">
  <div class="promo">
    <h4>SUB - HEADING</h4>
    <p>Lorem ipsum dolor sit amet, consectetuer adipiscing elit, sed diam nonummy nibh euismod tincidunt ut laoreet dolore magna aliquam erat volutpat. Ut wisi enim ad minim veniam, quis nostrud exerci tation ullamcorper suscipit lobortis nisl ut aliquip ex ea commodo consequat.</p>
    <span class="more">READ MORE</span>
  </div>
  <div class="promo">
    <h4>SUB - HEADING</h4>
    <div class="deal">10% OFF* ON FIRST<br>PURCHASING</div>
  </div>
</section>

<footer class="site-footer">
  <div class="f-col f-menu"><h5>Menu</h5><ul><li>Home</li><li>About</li><li>Products</li><li>Contact</li></ul></div>
  <div class="f-col" style="left:243px;width:295px"><h5>Categories</h5></div>
  <div class="f-col" style="left:243px;top:31px"><ul><li>Nav-01</li><li>Nav-02</li><li>Nav-03</li><li>Nav-04</li></ul></div>
  <div class="f-col" style="left:329px;top:31px"><ul><li>Nav-01</li><li>Nav-02</li><li>Nav-03</li><li>Nav-04</li></ul></div>
  <div class="f-col" style="left:412px;top:31px"><ul><li>Nav-01</li><li>Nav-02</li><li>Nav-03</li><li>Nav-04</li></ul></div>
  <div class="f-col" style="left:490px;top:31px"><ul><li>Nav-01</li><li>Nav-02</li><li>Nav-03</li><li>Nav-04</li></ul></div>
  <div class="f-box">Lorem ipsum dolor sit amet, consectetuer adipiscing elit, sed diam nonummy nibh euismod tincidunt ut laoreet dolore magna aliquam erat volutpat. Ut wisi enim ad minim veniam, quis nostrud exerci tation ullamcorper suscipit lobortis nisl ut aliquip ex ea commodo consequat.<span class="more">READ MORE</span></div>
</footer>
<div class="legal">All Right Reserved <b>Tossaro Inc.</b> 2012</div>

</body>
</html>
```